Residential home builder needs a fresh looking business card

We require a fresh looking business card for our business. We like the clean modern look. I have uploaded out logo and our email footer that incorporates some different elements. Blacks and Whites are good but i will leave this up to the design crowd creative minds.

our slogan is:
Built around the way you live

website (temporary site) but similar look and feel to the finished one
bluegumdwellings.com.au

We also have intentions to apply the same look and feel to the rest of our stationary (letterheads, envelopes, site signs, vehicles etc)

Home Builder

```html
<!DOCTYPE html>
<html lang="en">
<head>
<meta charset="utf-8">
<title>Bluegum Dwellings – Business Card</title>
<link href="https://fonts.googleapis.com/css2?family=Cinzel:wght@400&family=Open+Sans:wght@400;700&display=swap" rel="stylesheet">
<style>
  :root {
    --ink: #1a1a1a;
    --gold: #e8b320;
    --gold-soft: #f3de8f;
    --line-grey: #d9d9d9;
    --paper: #ffffff;
    --backdrop: #f2f2f2;
    --edge: #c8c8c8;
  }
  * { margin: 0; padding: 0; box-sizing: border-box; }
  html, body { width: 1200px; height: 1000px; overflow: hidden; background: var(--backdrop); }
  .canvas { position: relative; width: 1200px; height: 1000px; }
  .card-slot { position: absolute; left: 320px; width: 560px; height: 342px; }
  .card-slot.front { top: 148px; }
  .card-slot.back { top: 510px; }
  .card {
    position: absolute; left: 0; top: 0; width: 390px; height: 238px;
    transform: scale(1.4359); transform-origin: top left;
    background: var(--paper); border: 1px solid var(--edge); overflow: hidden;
    font-family: "Open Sans", Arial, sans-serif; color: var(--ink);
  }
  .brand {
    position: absolute; display: flex; align-items: center; gap: 5px;
    font-family: "Cinzel", Georgia, serif; font-weight: 400; color: var(--ink); white-space: nowrap;
  }
  .brand-square { background: var(--gold); display: block; }
  .front .brand { left: 16px; top: 56px; font-size: 12px; }
  .front .brand-square { width: 9px; height: 9px; }
  .blueprint {
    position: absolute; left: 102px; top: 4px; width: 288px; height: 82px;
    background: linear-gradient(90deg, rgba(255,255,255,0) 0%, rgba(232,232,232,0.6) 40%, rgba(243,222,143,0.35) 100%);
  }
  .blueprint-rule { position: absolute; left: 102px; top: 82px; width: 250px; height: 1px; background: var(--gold-soft); }
  .front .slogan {
    position: absolute; left: 151px; top: 42px; white-space: nowrap;
    font-family: "Cinzel", Georgia, serif; font-size: 10.5px; color: var(--gold); letter-spacing: 0.2px;
  }
  .holder-name { position: absolute; left: 17px; top: 119px; font-size: 15.5px; font-weight: 700; }
  .holder-title { position: absolute; left: 19px; top: 138px; font-size: 9.5px; font-weight: 700; }
  .contact { position: absolute; left: 161px; top: 162px; font-size: 9px; line-height: 11.6px; list-style: none; }
  .contact .label { color: var(--gold); font-weight: 700; }
  .contact .address { font-size: 8px; }
  .stripe { position: absolute; left: 0; width: 390px; height: 7px; }
  .front .stripe { top: 230px; }
  .back .stripe { top: 2px; }
  .back .brand { left: 0; right: 0; top: 104px; justify-content: center; font-size: 19px; }
  .back .brand-square { width: 14px; height: 14px; }
  .back .slogan {
    position: absolute; left: 0; right: 0; top: 174px; text-align: center; white-space: nowrap;
    font-family: "Cinzel", Georgia, serif; font-size: 10px; letter-spacing: 0.4px; color: var(--ink);
  }
</style>
</head>
<body>
<main class="canvas">
  <div class="card-slot front">
    <section class="card card-front">
      <div class="blueprint" role="img" aria-label="Faint line drawing of house outlines and floor plan"></div>
      <div class="blueprint-rule"></div>
      <div class="brand"><span class="brand-square"></span>Bluegum Dwellings</div>
      <p class="slogan">BUILT AROUND THE WAY YOU LIVE</p>
      <h1 class="holder-name">Marcus Holloway</h1>
      <p class="holder-title">General Manager</p>
      <ul class="contact">
        <li><span class="label">Mobile:</span> 0400 555 012</li>
        <li><span class="label">Phone:</span> 08 5550 0142 &nbsp;<span class="label">Fax:</span> 08 5550 0187</li>
        <li><span class="label">Email:</span> marcus@bluegumdwellings.com.au</li>
        <li><span class="label">Web:</span> www.bluegumdwellings.com.au</li>
        <li class="address">PO Box 418, Harbourview DC, WA 6990</li>
      </ul>
      <svg class="stripe" viewBox="0 0 390 7" aria-hidden="true">
        <polygon points="0,0 305,0 299,7 0,7" fill="var(--ink)"/>
        <polygon points="312,0 390,0 390,7 306,7" fill="var(--gold)"/>
      </svg>
    </section>
  </div>
  <div class="card-slot back">
    <section class="card card-back">
      <svg class="stripe" viewBox="0 0 390 7" aria-hidden="true">
        <polygon points="0,0 305,0 299,7 0,7" fill="var(--ink)"/>
        <polygon points="312,0 390,0 390,7 306,7" fill="var(--gold)"/>
      </svg>
      <div class="brand"><span class="brand-square"></span>Bluegum Dwellings</div>
      <p class="slogan">BUILT AROUND THE WAY YOU LIVE</p>
    </section>
  </div>
</main>
</body>
</html>
```